Business Card Design for my Real Estate Investing Company

This is for a Real Estate Investing Company that will be serving the Las Vegas Valley. Id like the following slogan included: "Investing in Our Community" I have attached my logo. You will see the color tones I'm interested in..in my logo. I would like the card to be double-sided with a modern, professional look.
Target Market(s)
Homeowners, banks, real estate industry
Industry/Entity Type
Real Estate
Contact Information for Business Card
name: Dale Pruitt
position: Managing Member
address: 4812 Corvane Pkwy ste 207-300
N. Las Vegas, NV 89517
phone: (702) 555-0143
fax: (702) 555-0187
email: OakridgeHousePurchaser@examplemail.com
web: OakridgeHousePurchasers.example
*At the bottom of the card I would like....
We buy houses for cash....no repairs, no commissions, no fees!
Logo Text
OAKRIDGE HOUSE PURCHASERS "Investing in Our Community"
Font styles to use
Other font styles liked:
- Lora
Requirements
Must have
- On the back of the card, i'd like to have my logo large and the following statements:
- Are you considering selling your home? Want a simple, hassle-free transaction? We can help! We buy houses for cash and can close quickly! No need to do any repairs, no realtor commissions, no closing costs.....and no headaches. Let us help you with your real estate needs...!
Nice to have
- multiple colors 2 two tone on front and back

```html
<!DOCTYPE html>
<html lang="en">
<head>
<meta charset="utf-8">
<title>Oakridge House Purchasers – Business Card</title>
<link rel="stylesheet" href="https://fonts.googleapis.com/css2?family=Lora:ital,wght@0,400;0,500;1,400;1,600&display=swap">
<style>
  :root {
    --brand-blue: #0756a5;
    --card-grey: #d9dadb;
    --mark-grey: #9a9b9d;
    --ink: #222326;
    --white: #ffffff;
    --page: #e6e7e7;
  }
  * { box-sizing: border-box; margin: 0; padding: 0; }
  html, body { width: 1200px; height: 1200px; overflow: hidden; }
  body {
    background: var(--page);
    font-family: "Lora", Georgia, serif;
    position: relative;
  }
  .card {
    position: absolute;
    left: 250px;
    width: 700px;
    height: 420px;
    overflow: hidden;
  }
  .card--front { top: 150px; background: var(--brand-blue); color: var(--white); }
  .card--back { top: 630px; background: var(--card-grey); color: var(--ink); }

  .brand {
    position: absolute;
    left: 60px;
    top: 62px;
    width: 360px;
    z-index: 2;
  }
  .brand__name {
    display: flex;
    align-items: center;
    gap: 14px;
    font-weight: 400;
    font-size: 30px;
    line-height: 1.1;
    letter-spacing: 0.5px;
  }
  .brand__square { width: 16px; height: 16px; flex: none; }
  .card--front .brand__name { color: var(--white); }
  .card--front .brand__square { background: var(--white); }
  .card--back .brand__name { color: var(--brand-blue); }
  .card--back .brand__square { background: var(--brand-blue); }
  .brand__slogan {
    margin-top: 10px;
    font-style: italic;
    font-weight: 600;
    font-size: 12px;
    letter-spacing: 5px;
    white-space: nowrap;
  }

  .person {
    position: absolute;
    right: 50px;
    top: 108px;
    text-align: center;
    font-style: italic;
    font-weight: 600;
    z-index: 2;
  }
  .person__name { font-size: 31px; line-height: 1.15; }
  .person__title { font-size: 20px; }
  .card--back .person { color: var(--brand-blue); }

  .divider {
    position: absolute;
    left: 0; right: 0;
    top: 188px;
    height: 4px;
  }
  .card--front .divider { background: var(--white); }
  .card--back .divider { background: var(--brand-blue); }

  .contacts {
    position: absolute;
    right: 36px;
    top: 218px;
    list-style: none;
    font-style: italic;
    font-size: 17.5px;
    text-align: right;
    z-index: 2;
  }
  .contacts li { height: 50px; display: flex; justify-content: flex-end; align-items: flex-start; gap: 54px; }
  .contact { display: inline-flex; align-items: center; gap: 6px; white-space: nowrap; }
  .contact svg { width: 14px; height: 14px; flex: none; }

  .skyline-area {
    position: absolute;
    bottom: 0;
    height: 170px;
    z-index: 1;
  }
  .card--front .skyline-area {
    left: 0;
    width: 340px;
    background: linear-gradient(160deg, #c9d3df 0%, #e9edf2 55%, #ffffff 100%);
    clip-path: polygon(0 0, 28% 0, 100% 100%, 0 100%);
  }
  .card--back .skyline-area {
    right: 0;
    width: 370px;
    background: linear-gradient(200deg, #a9b6c6 0%, #e6e9ed 55%, #ffffff 100%);
    clip-path: polygon(72% 0, 100% 0, 100% 100%, 0 100%);
  }

  .pitch {
    position: absolute;
    left: 58px;
    top: 208px;
    font-style: italic;
    font-size: 17.5px;
    line-height: 28px;
    color: var(--ink);
    z-index: 2;
  }
</style>
</head>
<body>

<section class="card card--front" aria-label="Business card front">
  <div class="brand">
    <div class="brand__name"><span class="brand__square"></span><span>OAKRIDGE HOUSE<br>PURCHASERS</span></div>
    <div class="brand__slogan">"Investing in Our Community"</div>
  </div>
  <div class="person">
    <div class="person__name">Dale Pruitt</div>
    <div class="person__title">Managing Member</div>
  </div>
  <div class="divider"></div>

  <ul class="contacts">
    <li><span class="contact">
      <svg viewBox="0 0 14 14"><circle cx="7" cy="7" r="7" fill="#fff"/><path d="M7 3a2.4 2.4 0 0 0-2.4 2.4C4.6 7.3 7 10.5 7 10.5s2.4-3.2 2.4-5.1A2.4 2.4 0 0 0 7 3z" fill="#0756a5"/></svg>
      4812 Corvane Pkwy ste 207-300&nbsp; N. Las Vegas, NV 89517</span></li>
    <li>
      <span class="contact">
        <svg viewBox="0 0 14 14"><circle cx="7" cy="7" r="7" fill="#fff"/><rect x="5" y="3.5" width="4" height="7" rx="1" fill="#0756a5"/></svg>
        (702) 555-0143</span>
      <span class="contact">
        <svg viewBox="0 0 14 14"><circle cx="7" cy="7" r="7" fill="#fff"/><rect x="4" y="4" width="6" height="6" rx="1" fill="none" stroke="#0756a5" stroke-width="1.4"/></svg>
        (702) 555-0187</span>
    </li>
    <li><span class="contact">
      <svg viewBox="0 0 14 14"><circle cx="7" cy="7" r="7" fill="#fff"/><rect x="3.5" y="4.5" width="7" height="5" fill="#0756a5"/></svg>
      OakridgeHousePurchaser@examplemail.com</span></li>
    <li><span class="contact">
      <svg viewBox="0 0 14 14"><circle cx="7" cy="7" r="7" fill="#fff"/><circle cx="7" cy="7" r="4" fill="none" stroke="#0756a5" stroke-width="1"/><path d="M3 7h8M7 3v8" stroke="#0756a5" stroke-width="1"/></svg>
      OakridgeHousePurchasers.example</span></li>
  </ul>

  <div class="skyline-area" role="img" aria-label="Decorative rooftop and city building illustration"></div>
</section>

<section class="card card--back" aria-label="Business card back">
  <div class="brand">
    <div class="brand__name"><span class="brand__square"></span><span>OAKRIDGE HOUSE<br>PURCHASERS</span></div>
    <div class="brand__slogan">"Investing in Our Community"</div>
  </div>
  <div class="person">
    <div class="person__name">Dale Pruitt</div>
    <div class="person__title">Managing Member</div>
  </div>
  <div class="divider"></div>

  <p class="pitch">
    Are you considering selling your home?<br>
    Want a simple, hassle-free transaction?&nbsp; We can help!<br>
    We buy houses for cash and can close quickly!<br>
    No need to do any repairs, no realtor<br>
    commissions, no closing costs.....<br>
    and no headaches. Let us help you<br>
    with your real estate needs...!
  </p>

  <div class="skyline-area" role="img" aria-label="Decorative rooftop and city building illustration"></div>
</section>

</body>
</html>
```